Start-Up Property Development Company Requires Word Press Website Design

A new property development company in Sydney requires a new website.
This version (Version 1) is very simple and will represent one, small aspect of what the company does, which is acquiring properties for redevelopment:

Needed:
- 1 page incorporating copy, logo and illustration.
- Email contact form.
- Contact information.

It will be expanded in the next few months to include another section for marketing homes for sale (Version 2). This section should sit on top of the Version 1 (in the top section of the same scrolling page).

So this initial design must be able to simply incorporate the expansion.

The site design needs to:
- Take up the entire width of the monitor.
- Not be too different from companies corporate look and feel.
- Be simple, functional and elegant.
- Have a long scroll (1 page) with navigation items at the top of the screen simply linking to the corresponding section lower in the page.

Reason: Not happy with the choice of designs. I'm wanting something clean and fresh and not too intensive with graphics.

```html
<!DOCTYPE html>
<html lang="en">
<head>
<meta charset="utf-8">
<title>Kestrel Property</title>
<link href="https://fonts.googleapis.com/css2?family=Open+Sans:wght@400;600;700&display=swap" rel="stylesheet">
<style>
  :root {
    --red: #d8242b;
    --black: #000000;
    --white: #ffffff;
    --ink: #1a1a1a;
    --field-border: #bdbdbd;
    --placeholder: #8c8c8c;
    --money-green: #8bb36a;
    --money-gold: #d9b76a;
  }
  * { box-sizing: border-box; margin: 0; padding: 0; }
  html, body { width: 847px; height: 1200px; overflow: hidden; background: var(--white); }
  body { font-family: "Open Sans", Arial, sans-serif; color: var(--ink); position: relative; }

  .shapes { position: absolute; inset: 0; width: 847px; height: 1200px; }

  .brand {
    position: absolute; left: 22px; top: 18px;
    display: flex; align-items: center; gap: 10px;
  }
  .brand-mark { width: 26px; height: 26px; background: var(--red); }
  .brand-name {
    font-weight: 700; font-size: 20px; line-height: 1; color: var(--black);
    letter-spacing: 0.5px;
  }

  .site-nav {
    position: absolute; left: 0; top: 90px; height: 37px;
    display: flex; align-items: center; gap: 34px; padding-left: 28px;
  }
  .site-nav a {
    color: var(--white); text-decoration: none; font-weight: 700; font-size: 14px;
    padding-bottom: 3px;
  }
  .site-nav a.is-current { border-bottom: 2px solid var(--white); }

  .intro-illustration {
    position: absolute; left: 14px; top: 160px; width: 325px; height: 265px;
    background: radial-gradient(ellipse at 50% 55%, var(--money-green) 0%, var(--money-gold) 45%, #eef0ea 75%, var(--white) 100%);
  }
  .intro-copy {
    position: absolute; left: 361px; top: 166px; width: 420px;
    font-size: 12.5px; line-height: 1.45; color: var(--ink);
  }
  .intro-copy p { margin-bottom: 13px; }

  .email-title {
    position: absolute; left: 28px; top: 530px;
    color: var(--white); font-size: 31px; font-weight: 400;
  }
  .email-form { position: absolute; left: 28px; top: 598px; width: 528px; }
  .field {
    display: block; width: 402px; height: 26px; margin-bottom: 15px;
    background: var(--black); border: 1px solid var(--field-border);
    color: var(--placeholder); font-family: inherit; font-size: 12px; padding: 4px 8px;
  }
  .field-message { height: 92px; resize: none; }
  .submit {
    position: absolute; left: 423px; top: 130px; width: 105px; height: 42px;
    background: var(--white); color: var(--black); border: none;
    font-family: inherit; font-weight: 700; font-size: 17px; letter-spacing: 0.5px;
  }

  .contact-title {
    position: absolute; left: 28px; top: 880px; font-size: 34px; font-weight: 400; color: var(--black);
  }
  .contact-col {
    position: absolute; top: 980px; font-size: 12px; line-height: 1.5; color: var(--ink); font-style: normal;
  }
  .contact-address { left: 28px; }
  .contact-phone { left: 344px; }
  .contact-email { left: 621px; }

  .site-footer {
    position: absolute; left: 0; top: 1143px; width: 847px; height: 57px;
    background: var(--black); color: var(--white);
    display: flex; align-items: center; justify-content: center;
    font-size: 10px; font-weight: 600;
  }
</style>
</head>
<body>
  <svg class="shapes" viewBox="0 0 847 1200" aria-hidden="true">
    <rect x="0" y="90" width="847" height="37" fill="var(--black)"/>
    <polygon points="579,0 847,0 847,170" fill="var(--red)"/>
    <rect x="0" y="474" width="847" height="373" fill="var(--black)"/>
    <polygon points="560,474 847,474 847,790" fill="var(--red)"/>
    <polygon points="470,847 847,710 847,847" fill="var(--white)"/>
  </svg>

  <header>
    <div class="brand">
      <span class="brand-mark"></span>
      <span class="brand-name">KESTREL PROPERTY</span>
    </div>
    <nav class="site-nav">
      <a href="#home" class="is-current">HOME</a>
      <a href="#contact">CONTACT INFO</a>
      <a href="#email">EMAIL US</a>
    </nav>
  </header>

  <section id="home">
    <div class="intro-illustration" role="img" aria-label="Illustration of a small house built from banknotes under a magnifying glass"></div>
    <div class="intro-copy">
      <p>Kestrel Property is a property development company located in Sydney. We are currently searching for properties to acquire and redevelop.</p>
      <p>We value properties using their potential value following redevelopment, rather than the commonly used methods of recent, comparative sales and the opinions of agents. Because of this we can sometimes offer more than what is typical for your local market.</p>
      <p>Kestrel Property is not a real estate agency, so you won't have to pay a real estate agents commission for the sale of your property should you decide to work with us.</p>
      <p>So if you're thinking of selling or interested in knowing what we think your property is worth, please contact us!</p>
    </div>
  </section>

  <section id="email">
    <h2 class="email-title">Email Us</h2>
    <form class="email-form">
      <input class="field" type="text" placeholder="Name">
      <input class="field" type="email" placeholder="Email">
      <textarea class="field field-message" placeholder="Message"></textarea>
      <button class="submit" type="button">SUBMIT</button>
    </form>
  </section>

  <section id="contact">
    <h2 class="contact-title">Contact</h2>
    <address class="contact-col contact-address">Kestrel Pty Ltd<br>P.O. Box 81<br>Redfern NSW 2016</address>
    <div class="contact-col contact-phone">Tel: 02 9555 0148<br>Mob: 0400 555 217</div>
    <div class="contact-col contact-email">hello@kestrelproperty.example</div>
  </section>

  <footer class="site-footer">Copyright - Kestrel Pty Ltd</footer>
</body>
</html>
```